Clean bold and classy business card front and back
Kwr can be the logo
My name Trent Holloman as owner
Phone email and address
Owner Trent Holloman
Phone 8505550147
Email ridgelineinsulate@mailnest.example
Address170 frank pais rd Havana fl 32399

Industry/Entity Type

Business

Contact Information for Business Card

Owner Trent Holloman
Phone 8505550147

Requirements
Must have
• Keystone wall render under Kwr logo
Nice to have
• Bold and clean. Maybe use Kwr as logo and name under it. Have logo on one side and info on the other side with logo also
• Put a pic up. It doesn't have to be that but something that can be used
• Try some fancy fonts also

```html
<!DOCTYPE html>
<html lang="en">
<head>
<meta charset="utf-8">
<title>Keystone Wall Render – Business Card</title>
<link rel="stylesheet" href="https://fonts.googleapis.com/css2?family=Anton&family=Roboto:wght@400;700&display=swap">
<style>
  :root {
    --brand-blue: #0553a6;
    --card-white: #ffffff;
    --backdrop: #ebe6de;
    --card-shadow: rgba(0, 0, 0, 0.28);
  }
  * { box-sizing: border-box; margin: 0; padding: 0; }
  html, body {
    width: 1189px;
    height: 1200px;
    overflow: hidden;
    background: var(--backdrop);
  }
  .canvas {
    position: relative;
    width: 1189px;
    height: 1200px;
  }
  .card {
    position: absolute;
    top: 145px;
    width: 482px;
    height: 845px;
    background: var(--card-white);
    box-shadow: 6px 8px 14px var(--card-shadow);
    color: var(--brand-blue);
    text-align: center;
  }
  .card--front { left: 74px; }
  .card--back { left: 630px; }

  .brand-mark {
    position: absolute;
    left: 0;
    right: 0;
    font-family: "Anton", sans-serif;
    font-weight: 400;
    color: var(--brand-blue);
    line-height: 1;
  }
  .brand-mark__initials {
    display: block;
    font-size: 150px;
    letter-spacing: 4px;
  }
  .brand-mark__name {
    display: block;
    margin-top: 14px;
    font-size: 29px;
    letter-spacing: 3px;
    text-transform: uppercase;
  }
  .card--front .brand-mark { top: 300px; }
  .card--back .brand-mark { top: 82px; }

  .owner {
    position: absolute;
    top: 405px;
    left: 0;
    right: 0;
  }
  .owner__name {
    font-family: "Anton", sans-serif;
    font-size: 44px;
    font-weight: 400;
    line-height: 1.1;
  }
  .owner__role {
    font-family: "Roboto", sans-serif;
    font-size: 30px;
    font-weight: 400;
    line-height: 1.1;
  }

  .contact {
    position: absolute;
    top: 580px;
    left: 0;
    right: 0;
    font-family: "Roboto", sans-serif;
  }
  .contact__phone {
    font-size: 43px;
    font-weight: 400;
    line-height: 1.1;
  }
  .contact__email {
    margin-top: 8px;
    font-size: 20px;
    font-weight: 400;
  }

  .address-band {
    position: absolute;
    left: 0;
    right: 0;
    bottom: 0;
    height: 80px;
    background: var(--brand-blue);
    color: var(--card-white);
    font-family: "Roboto", sans-serif;
    font-weight: 700;
    font-size: 21px;
    letter-spacing: 1px;
    word-spacing: 4px;
    display: flex;
    align-items: center;
    justify-content: center;
  }
</style>
</head>
<body>
  <main class="canvas">
    <section class="card card--front" aria-label="Card front">
      <div class="brand-mark">
        <span class="brand-mark__initials">KWR</span>
        <span class="brand-mark__name">Keystone Wall Render</span>
      </div>
    </section>

    <section class="card card--back" aria-label="Card back">
      <div class="brand-mark">
        <span class="brand-mark__initials">KWR</span>
        <span class="brand-mark__name">Keystone Wall Render</span>
      </div>

      <div class="owner">
        <h1 class="owner__name">Trent Holloman</h1>
        <p class="owner__role">Owner</p>
      </div>

      <div class="contact">
        <p class="contact__phone">8505550147</p>
        <p class="contact__email">ridgelineinsulate@mailnest.example</p>
      </div>

      <footer class="address-band">428 dunmore ct Havana fl 32399</footer>
    </section>
  </main>
</body>
</html>
```